Innovative IT Service Provider seeks engaging overview presentation to capture new business

*Please see attached Creative Brief for full details*

Overall Goals
The goal of this presentation is to provide new, prospective clients with an introduction to Harborline Systems, the services we provide, and what makes us a unique and superior choice for their IT Services. The deck should be able to clearly relay this information while clients review it on their own, without further explanation from a company representative.

Design Goals
We are looking for a professional, modern, streamlined, sleek design that reflects our status as a leader in information technology and innovation.

Company Overview
As an IT Managed Service Provider, companies choose to outsource some or all of their internal IT functions to us to take advantage of our many areas of expertise and so they can focus on their core business, whatever industry they may be in. We also specialize in IT Cyber Security and Consulting, always providing our clients with thought leadership and insight into the latest IT innovations. We ultimately find ways to deliver value to our clients through our various IT solutions.

```html
<!DOCTYPE html>
<html lang="en">
<head>
<meta charset="utf-8">
<title>Harborline Systems – Process Driven</title>
<link rel="stylesheet" href="https://fonts.googleapis.com/css2?family=Open+Sans:wght@400;600;700&display=swap">
<style>
  :root {
    --band: #d9d9d9;
    --page: #ffffff;
    --navy: #1f3864;
    --title: #17375e;
    --ink: #262626;
    --muted: #595959;
    --lane-line: #8c8c8c;
    --box-grey: #4d4d4d;
    --header-grey: #3f3f3f;
    --header-red: #8e1b1b;
    --accent-red: #b8332f;
  }
  * { box-sizing: border-box; margin: 0; padding: 0; }
  html, body { width: 1200px; height: 675px; overflow: hidden; background: var(--page); }
  body { font-family: "Open Sans", Arial, sans-serif; color: var(--ink); }

  .slide { position: relative; width: 1200px; height: 675px; background: var(--page); overflow: hidden; }

  .top-band { position: absolute; left: 0; top: 0; width: 1200px; height: 87px; background: var(--band); }
  .bottom-band { position: absolute; left: 0; bottom: 0; width: 1200px; height: 72px; background: var(--band); }

  .brand { position: absolute; left: 45px; top: 20px; display: flex; align-items: center; gap: 12px; }
  .brand-mark { width: 34px; height: 34px; background: var(--navy); }
  .brand-name { font-weight: 700; font-size: 22px; letter-spacing: 1px; color: var(--navy); text-transform: uppercase; line-height: 1; }

  .slide-title { position: absolute; left: 45px; top: 118px; font-size: 30px; font-weight: 700; color: var(--title); }

  .checklist { position: absolute; left: 55px; top: 192px; list-style: none; }
  .checklist li { display: flex; align-items: center; height: 45px; font-size: 25px; color: var(--ink); }
  .checklist .tick { width: 22px; height: 22px; margin-right: 12px; flex: none; }

  .diagram { position: absolute; background: #fff; box-shadow: 2px 3px 8px rgba(0,0,0,0.35); }
  .diagram-ticket { left: 850px; top: 113px; width: 327px; height: 292px; }
  .diagram-kba { left: 550px; top: 328px; width: 358px; height: 230px; }
  .diagram svg { display: block; }
  .diagram text { font-family: "Open Sans", Arial, sans-serif; }
</style>
</head>
<body>
<div class="slide">
  <div class="top-band"></div>
  <div class="brand">
    <span class="brand-mark"></span>
    <span class="brand-name">Harborline Systems</span>
  </div>

  <h1 class="slide-title">Process Driven</h1>

  <ul class="checklist">
    <li><svg class="tick" viewBox="0 0 22 22"><path d="M3 12 L9 18 L19 3" fill="none" stroke="#262626" stroke-width="2.2" stroke-linecap="round" stroke-linejoin="round"/></svg>Continuous Service Improvement</li>
    <li><svg class="tick" viewBox="0 0 22 22"><path d="M3 12 L9 18 L19 3" fill="none" stroke="#262626" stroke-width="2.2" stroke-linecap="round" stroke-linejoin="round"/></svg>Service Quality Process</li>
    <li><svg class="tick" viewBox="0 0 22 22"><path d="M3 12 L9 18 L19 3" fill="none" stroke="#262626" stroke-width="2.2" stroke-linecap="round" stroke-linejoin="round"/></svg>Knowledge Management Process</li>
    <li><svg class="tick" viewBox="0 0 22 22"><path d="M3 12 L9 18 L19 3" fill="none" stroke="#262626" stroke-width="2.2" stroke-linecap="round" stroke-linejoin="round"/></svg>Mature Onboarding Process</li>
  </ul>

  <!-- Ticket workflow swimlane chart -->
  <div class="diagram diagram-ticket">
    <svg width="327" height="292" viewBox="0 0 327 292">
      <defs>
        <marker id="arrowA" viewBox="0 0 6 6" refX="5" refY="3" markerWidth="5" markerHeight="5" orient="auto"><path d="M0 0 L6 3 L0 6 Z" fill="#404040"/></marker>
      </defs>
      <rect x="0" y="0" width="327" height="13" fill="var(--header-red)"/>
      <text x="6" y="10" font-size="8" font-weight="700" fill="#fff">Unbundled Ticket Process</text>
      <rect x="0" y="13" width="18" height="279" fill="var(--navy)"/>
      <line x1="0" y1="47" x2="327" y2="47" stroke="var(--lane-line)" stroke-width="1"/>
      <line x1="0" y1="122" x2="327" y2="122" stroke="var(--lane-line)" stroke-width="1"/>
      <text transform="translate(12 36) rotate(-90)" font-size="6" fill="#fff">Client</text>
      <text transform="translate(12 100) rotate(-90)" font-size="6" fill="#fff">Service Desk</text>
      <text transform="translate(12 230) rotate(-90)" font-size="6" fill="#fff">Field Team</text>

      <rect x="24" y="20" width="40" height="13" rx="6.5" fill="var(--header-red)"/>
      <text x="44" y="29" font-size="4.5" fill="#fff" text-anchor="middle">Needs support</text>
      <line x1="64" y1="26" x2="90" y2="26" stroke="#404040" marker-end="url(#arrowA)"/>
      <rect x="92" y="18" width="18" height="13" fill="#fff" stroke="var(--navy)"/>
      <path d="M92 18 L101 26 L110 18" fill="none" stroke="var(--navy)"/>
      <text x="101" y="40" font-size="4.5" fill="var(--navy)" text-anchor="middle">help@client.example</text>

      <rect x="24" y="65" width="32" height="18" fill="var(--navy)"/>
      <text x="40" y="76" font-size="4.5" fill="#fff" text-anchor="middle">Log ticket</text>
      <line x1="56" y1="74" x2="90" y2="74" stroke="#404040" marker-end="url(#arrowA)"/>
      <rect x="92" y="65" width="32" height="18" fill="var(--box-grey)"/>
      <text x="108" y="76" font-size="4.5" fill="#fff" text-anchor="middle">Assess</text>
      <line x1="124" y1="74" x2="136" y2="74" stroke="#404040" marker-end="url(#arrowA)"/>
      <rect x="138" y="65" width="32" height="18" fill="var(--box-grey)"/>
      <text x="154" y="76" font-size="4.5" fill="#fff" text-anchor="middle">Quote</text>
      <line x1="170" y1="74" x2="172" y2="74" stroke="#404040"/>
      <rect x="174" y="65" width="32" height="18" fill="var(--box-grey)"/>
      <text x="190" y="76" font-size="4.5" fill="#fff" text-anchor="middle">Approve</text>
      <rect x="96" y="90" width="22" height="26" fill="var(--accent-red)"/>
      <rect x="99" y="93" width="16" height="5" fill="#fff"/>
      <g fill="#fff">
        <rect x="99" y="101" width="4" height="3"/><rect x="105" y="101" width="4" height="3"/><rect x="111" y="101" width="4" height="3"/>
        <rect x="99" y="106" width="4" height="3"/><rect x="105" y="106" width="4" height="3"/><rect x="111" y="106" width="4" height="3"/>
        <rect x="99" y="111" width="4" height="3"/><rect x="105" y="111" width="4" height="3"/><rect x="111" y="111" width="4" height="3"/>
      </g>
      <line x1="40" y1="83" x2="40" y2="136" stroke="#404040" marker-end="url(#arrowA)"/>

      <rect x="24" y="138" width="32" height="18" fill="var(--navy)"/>
      <text x="40" y="149" font-size="4.5" fill="#fff" text-anchor="middle">Dispatch</text>
      <line x1="56" y1="147" x2="75" y2="147" stroke="#404040" marker-end="url(#arrowA)"/>
      <path d="M87 136 L98 147 L87 158 L76 147 Z" fill="var(--navy)"/>
      <line x1="98" y1="147" x2="120" y2="147" stroke="#404040" marker-end="url(#arrowA)"/>
      <rect x="122" y="138" width="32" height="18" fill="var(--navy)"/>
      <text x="138" y="149" font-size="4.5" fill="#fff" text-anchor="middle">Resolve</text>
      <line x1="154" y1="147" x2="148" y2="147" stroke="#404040"/>
      <line x1="154" y1="147" x2="147" y2="147" stroke="#404040"/>
      <line x1="154" y1="147" x2="148" y2="147" stroke="#404040"/>
      <line x1="154" y1="147" x2="148" y2="147" stroke="#404040"/>
      <path d="M168 136 L179 147 L168 158 L157 147 Z" fill="var(--navy)"/>
      <line x1="179" y1="147" x2="195" y2="147" stroke="#404040" marker-end="url(#arrowA)"/>
      <rect x="197" y="138" width="34" height="18" fill="var(--navy)"/>
      <text x="214" y="149" font-size="4.5" fill="#fff" text-anchor="middle">Close out</text>
      <line x1="168" y1="158" x2="168" y2="176" stroke="#404040" marker-end="url(#arrowA)"/>
      <rect x="152" y="178" width="34" height="18" fill="var(--navy)"/>
      <text x="169" y="189" font-size="4.5" fill="#fff" text-anchor="middle">Follow up</text>
      <line x1="186" y1="187" x2="197" y2="187" stroke="#404040" marker-end="url(#arrowA)"/>
      <path d="M210 176 L221 187 L210 198 L199 187 Z" fill="var(--navy)"/>
      <line x1="221" y1="187" x2="235" y2="187" stroke="#404040" marker-end="url(#arrowA)"/>
    </svg>
  </div>

  <!-- Knowledge article improvement swimlane chart -->
  <div class="diagram diagram-kba">
    <svg width="358" height="230" viewBox="0 0 358 230">
      <defs>
        <marker id="arrowB" viewBox="0 0 6 6" refX="5" refY="3" markerWidth="5" markerHeight="5" orient="auto"><path d="M0 0 L6 3 L0 6 Z" fill="#404040"/></marker>
      </defs>
      <rect x="0" y="0" width="358" height="17" fill="var(--header-grey)"/>
      <text x="7" y="12" font-size="8" font-weight="700" fill="#fff">KBA Improvement</text>
      <rect x="0" y="17" width="20" height="213" fill="var(--navy)"/>
      <line x1="0" y1="83" x2="358" y2="83" stroke="var(--lane-line)" stroke-width="1"/>
      <line x1="0" y1="155" x2="358" y2="155" stroke="var(--lane-line)" stroke-width="1"/>
      <text transform="translate(13 62) rotate(-90)" font-size="6" fill="#fff">Client or IS</text>
      <text transform="translate(13 137) rotate(-90)" font-size="6" fill="#fff">Service Desk</text>
      <text transform="translate(13 218) rotate(-90)" font-size="6" fill="#fff">Knowledge Team</text>

      <rect x="38" y="56" width="44" height="13" rx="6.5" fill="var(--header-grey)"/>
      <text x="60" y="65" font-size="4.5" fill="#fff" text-anchor="middle">Wants new article</text>
      <line x1="82" y1="62" x2="168" y2="62" stroke="#404040" marker-end="url(#arrowB)"/>
      <rect x="170" y="42" width="24" height="18" fill="#fff" stroke="var(--navy)"/>
      <path d="M170 42 L182 52 L194 42" fill="none" stroke="var(--navy)"/>
      <text x="182" y="70" font-size="5" fill="var(--navy)" text-anchor="middle">kb@client.example</text>
      <line x1="48" y1="69" x2="48" y2="106" stroke="#404040" marker-end="url(#arrowB)"/>

      <g font-size="4.5" fill="#fff" text-anchor="middle">
        <rect x="40" y="108" width="34" height="25" fill="var(--navy)"/>
        <text x="57" y="122" fill="#fff">Create ticket</text>
        <rect x="100" y="108" width="34" height="25" fill="var(--navy)"/>
        <text x="117" y="122" fill="#fff">Triage</text>
        <rect x="157" y="108" width="34" height="25" fill="var(--navy)"/>
        <text x="174" y="122" fill="#fff">Reply to user</text>
        <rect x="214" y="108" width="34" height="25" fill="var(--navy)"/>
        <text x="231" y="122" fill="#fff">Move ticket</text>
        <rect x="271" y="108" width="34" height="25" fill="var(--navy)"/>
        <text x="288" y="122" fill="#fff">Notify team</text>

        <rect x="40" y="176" width="34" height="25" fill="var(--navy)"/>
        <text x="57" y="190" fill="#fff">Receive request</text>
        <rect x="100" y="176" width="34" height="25" fill="var(--navy)"/>
        <text x="117" y="190" fill="#fff">Research</text>
        <rect x="157" y="176" width="34" height="25" fill="var(--navy)"/>
        <text x="174" y="190" fill="#fff">Draft KBA</text>
        <rect x="214" y="176" width="34" height="25" fill="var(--navy)"/>
        <text x="231" y="190" fill="#fff">Get approval</text>
        <rect x="271" y="176" width="34" height="25" fill="var(--navy)"/>
        <text x="288" y="190" fill="#fff">Publish KBA</text>
      </g>
      <g stroke="#404040" fill="none">
        <line x1="74" y1="120" x2="98" y2="120" marker-end="url(#arrowB)"/>
        <line x1="134" y1="120" x2="155" y2="120" marker-end="url(#arrowB)"/>
        <line x1="191" y1="120" x2="212" y2="120" marker-end="url(#arrowB)"/>
        <line x1="248" y1="120" x2="269" y2="120" marker-end="url(#arrowB)"/>
        <path d="M288 133 L288 150 L57 150 L57 174" marker-end="url(#arrowB)"/>
        <line x1="74" y1="188" x2="98" y2="188" marker-end="url(#arrowB)"/>
        <line x1="134" y1="188" x2="155" y2="188" marker-end="url(#arrowB)"/>
        <line x1="191" y1="188" x2="212" y2="188" marker-end="url(#arrowB)"/>
        <line x1="248" y1="188" x2="269" y2="188" marker-end="url(#arrowB)"/>
        <path d="M305 188 L330 188 L330 214 L30 214 L30 188 L38 188" marker-end="url(#arrowB)"/>
      </g>
    </svg>
  </div>

  <div class="bottom-band"></div>
</div>
</body>
</html>
```